BBQ Catering & Pop-up Restaurant

I'm a catering company and a pop-up restaurant and need a website that will have the following at minimum (I'm open to suggestions): about me section, menu section, events section, a pre-order page. Here is an example of a site that I really like ... https://hollowcreeksmokehouse.example/ . I want to have a pre-order page where people can place orders online and the ability to take credit card payments. I've included a word doc with a draft write up to get started.
Updates

Reason: I am awaiting feedback from my partner and will be in touch ASAP.

Target Market(s)

BBQ Lovers

Industry/Entity Type

Caterer

Font styles to use
Serif
Other font styles liked:
• we can use multiple fonts where appropriate. I also like a faded, woody type font - which reminds me of the old western movies

Colors

Designer to choose colors to be used in the design.

Requirements
Must have
• I want
• - a smokey, woody, bbq type feel to the site.
• - my logo to be utilized
• - colors I like should compliment the colors in my logo
• - link to sign up for a news letter/ mailing list and something on the back end to capture data
Nice to have
• NA
Should not have
• NA

```html
<!DOCTYPE html>
<html lang="en">
<head>
<meta charset="utf-8">
<title>Ember Ridge Smokehouse</title>
<link href="https://fonts.googleapis.com/css2?family=IM+Fell+English&family=Libre+Baskerville:wght@700&family=Open+Sans:wght@400;600&family=Roboto:wght@400;500&display=swap" rel="stylesheet">
<style>
:root{
  --red:#a3201f;
  --red-dark:#8b1a19;
  --gold:#f3d88a;
  --ring:#e3c22f;
  --ink:#333;
  --grey:#555;
  --muted:#7a7a7a;
  --wood:#eeeeec;
  --white:#fff;
  --footer:#1c1c1c;
  --footer-text:#d8d8d8;
}
*{box-sizing:border-box;margin:0;padding:0}
html,body{width:1200px;height:3297px;overflow:hidden}
body{position:relative;font-family:"Open Sans",sans-serif;color:var(--ink);background:var(--white)}
.section{position:absolute;left:0;width:1200px}
.heading{font-family:"IM Fell English",serif;font-size:44px;color:#555;text-align:center;position:absolute;left:0;width:1200px;font-weight:400}
.hero{top:0;height:666px;background:radial-gradient(ellipse at 75% 60%,#a34411 0%,#3a1a0c 35%,#141010 70%);}
.hero-photo{position:absolute;inset:0;background:radial-gradient(ellipse 420px 240px at 330px 380px,#6e3a26 0%,#4a2418 55%,transparent 100%),linear-gradient(180deg,rgba(0,0,0,.35),rgba(0,0,0,0) 30%,rgba(0,0,0,.4))}
.brand{position:absolute;left:99px;top:80px;display:flex;align-items:center;gap:12px;font-family:"Libre Baskerville",serif;font-weight:700;font-size:24px;color:var(--gold);width:240px;line-height:1.2}
.brand .mark{width:18px;height:18px;background:var(--red);flex:none}
.phone{position:absolute;left:905px;top:52px;color:var(--white);font-family:"Libre Baskerville",serif;font-weight:700;font-size:21px;display:flex;align-items:center;gap:10px}
.nav{position:absolute;left:574px;top:96px;display:flex;gap:30px;font-family:"Libre Baskerville",serif;font-weight:700;font-size:19px;color:var(--white)}
.hero-title{position:absolute;left:694px;top:290px;font-family:"Libre Baskerville",serif;font-weight:700;font-size:52px;line-height:1.25;color:var(--gold);width:400px}
.arrow{position:absolute;top:342px;width:36px;height:36px;border-radius:50%;background:rgba(0,0,0,.55);display:flex;align-items:center;justify-content:center}
.about{top:666px;height:374px;background:linear-gradient(90deg,#ececea,#f4f4f2,#e8e8e6)}
.about .heading{top:80px}
.about-text{position:absolute;left:171px;width:862px;top:152px;text-align:center;font-size:12.5px;line-height:24px;color:var(--grey)}
.btn{position:absolute;background:var(--red);color:var(--white);font-family:"Libre Baskerville",serif;font-weight:700;font-size:14px;display:flex;align-items:center;justify-content:center}
.read-more{left:549px;top:945px;width:104px;height:32px}
.order{top:1040px;height:668px;background:var(--red)}
.order .heading{top:62px;color:#f1b9a6}
.card{position:absolute;top:169px;width:462px;height:408px;background:var(--white);border:4px solid var(--white);box-shadow:0 2px 8px rgba(0,0,0,.35)}
.card-photo{height:216px}
.card-icon{position:absolute;left:205px;top:200px;width:48px;height:48px;border-radius:50%;background:var(--red);border:3px solid var(--white);display:flex;align-items:center;justify-content:center}
.card h3{font-family:"IM Fell English",serif;font-weight:400;font-size:26px;color:#333;text-align:center;margin-top:38px}
.card p{font-size:12px;line-height:20px;color:var(--grey);text-align:center;padding:6px 28px 0}
.menu{top:1708px;height:716px;background:linear-gradient(90deg,#ececea,#f5f5f3,#e9e9e7)}
.menu .heading{top:84px}
.menu-intro{position:absolute;left:200px;width:800px;top:150px;text-align:center;font-size:12px;line-height:22px;color:var(--grey)}
.dish{position:absolute;top:246px;width:264px;text-align:center}
.dish-photo{width:220px;height:220px;margin:0 auto;border-radius:50%;border:9px solid var(--ring);display:flex;align-items:center;justify-content:center}
.dish h4{font-family:"Libre Baskerville",serif;font-weight:700;font-size:19px;color:#444;margin-top:28px}
.dish .price{font-family:"Libre Baskerville",serif;font-weight:700;font-size:18px;color:var(--red);margin-top:10px}
.dish p{font-size:11.5px;line-height:19px;color:var(--grey);margin-top:12px;padding:0 24px}
.soon{font-family:"IM Fell English",serif;font-size:34px;color:var(--white);line-height:1.05}
.events{top:2424px;height:411px;background:var(--white)}
.events .heading{top:62px}
.event{position:absolute;top:160px;width:320px}
.event-thumb{position:absolute;left:0;top:0;width:70px;height:70px}
.event-name{position:absolute;left:86px;top:0;font-family:"Roboto",sans-serif;font-size:18px;color:var(--red)}
.event-city{position:absolute;left:86px;top:28px;font-size:10px;color:var(--muted)}
.event-date{position:absolute;left:86px;top:50px;font-family:"Roboto",sans-serif;font-weight:500;font-size:19px;color:#222}
.event p{position:absolute;left:0;top:88px;width:310px;font-size:11px;line-height:16px;color:var(--muted)}
.dots{position:absolute;top:340px;left:554px;display:flex;gap:14px}
.dots span{width:12px;height:12px;border-radius:50%;background:#c9c9c9}
.dots span:first-child{background:var(--red)}
.newsletter{top:2835px;height:95px;background:var(--red)}
.newsletter h2{position:absolute;left:121px;top:34px;font-family:"Libre Baskerville",serif;font-weight:700;font-size:20px;color:var(--white);white-space:nowrap;width:340px}
.email{position:absolute;left:479px;top:29px;width:438px;height:40px;background:var(--white);font-size:13px;color:#777;padding:12px 12px}
.join{left:932px;top:29px;width:143px;height:40px;background:#222;font-size:15px}
.footer{top:2930px;height:367px;background:#1b1b1b linear-gradient(180deg,#222,#161616)}
.footer .brand{top:86px;color:var(--gold)}
.col{position:absolute;top:62px;color:var(--footer-text);font-size:13px;line-height:24px}
.col h5{font-family:"Libre Baskerville",serif;font-weight:700;font-size:19px;color:var(--white);margin-bottom:18px}
.contact-row{display:flex;gap:18px;margin-bottom:18px;align-items:flex-start}
.contact-row svg{flex:none;margin-top:4px}
.copyright{position:absolute;left:99px;top:326px;font-size:11.5px;color:var(--footer-text)}
.social{position:absolute;left:960px;top:320px;display:flex;gap:12px}
.social span{width:20px;height:20px;border-radius:50%;background:var(--white)}
</style>
</head>
<body>

<header class="section hero">
  <div class="hero-photo" role="img" aria-label="Seasoned steak with rosemary and peppercorns on a smoky flaming grill"></div>
  <div class="brand"><span class="mark"></span>Ember Ridge Smokehouse</div>
  <div class="phone">
    <svg width="18" height="18" viewBox="0 0 24 24"><path fill="#fff" d="M6.6 10.8a15.1 15.1 0 0 0 6.6 6.6l2.2-2.2a1 1 0 0 1 1-.25 11.4 11.4 0 0 0 3.6.57 1 1 0 0 1 1 1V20a1 1 0 0 1-1 1A17 17 0 0 1 3 4a1 1 0 0 1 1-1h3.5a1 1 0 0 1 1 1c0 1.25.2 2.45.57 3.57a1 1 0 0 1-.25 1z"/></svg>
    555-310-4827
    <svg width="20" height="20" viewBox="0 0 24 24" style="margin-left:14px"><circle cx="10" cy="10" r="6.5" fill="none" stroke="#fff" stroke-width="2.6"/><path d="M15 15l6 6" stroke="#fff" stroke-width="2.8"/></svg>
  </div>
  <nav class="nav"><span>Home</span><span>About me</span><span>Menu Events</span><span>Preorder</span><span>Contact us</span></nav>
  <h1 class="hero-title">Ember Ridge Smoke House BBQ</h1>
  <div class="arrow" style="left:37px"><svg width="12" height="14" viewBox="0 0 12 14"><path d="M9 1L3 7l6 6" fill="none" stroke="#fff" stroke-width="2.5"/></svg></div>
  <div class="arrow" style="left:1107px"><svg width="12" height="14" viewBox="0 0 12 14"><path d="M3 1l6 6-6 6" fill="none" stroke="#fff" stroke-width="2.5"/></svg></div>
</header>

<section class="section about">
  <h2 class="heading">What Are We?</h2>
  <p class="about-text">Until recently, I've been a guy that sells smoked ribs to family and friends on the weekends. We're talking ONE-MAN-SHOW – it's been a lot of fun, but super exhausting.  Alhamdulillah, I've received overwhelmingly positive feedback on the ribs and I've been receiving a lot of new order requests from folks as well as a lot of repeat customers (this is always a good sign). So nooow, I'm a guy that sells ribs on the weekends to family and friends...and friends of family... and friends of friends – so basically nothing has changed...but they're about to, keep reading...</p>
</section>
<div class="btn read-more">Read More</div>

<section class="section order">
  <h2 class="heading">How Can You Order From Us?</h2>
  <article class="card" style="left:116px">
    <div class="card-photo" role="img" aria-label="Burger patties grilling over open flames" style="background:radial-gradient(ellipse at 50% 70%,#e0701c,#7a2a10 55%,#2a120a)"></div>
    <div class="card-icon"><svg width="18" height="22" viewBox="0 0 18 22"><path d="M9 1c1 4 7 7 7 13a7 7 0 0 1-14 0c0-3 2-5 3-6 0 2 1 3 2 3 0-4 1-7 2-10z" fill="#f5c24a"/></svg></div>
    <h3>Option #1</h3>
    <p>We have a minimum party requirement of 5 lbs. on meat orders with at least 48 hour advance notice, the sooner the better, this will allow us to ensure we have ribs in stock for you. Currently, we take orders for weekends only.</p>
  </article>
  <article class="card" style="left:622px">
    <div class="card-photo" role="img" aria-label="Peppered steak on a fork over a dark grill" style="background:radial-gradient(ellipse at 55% 65%,#7a3a28,#2c1a18 55%,#111)"></div>
    <div class="card-icon"><svg width="18" height="22" viewBox="0 0 18 22"><path d="M9 1c1 4 7 7 7 13a7 7 0 0 1-14 0c0-3 2-5 3-6 0 2 1 3 2 3 0-4 1-7 2-10z" fill="#f5c24a"/></svg></div>
    <h3>Option #2</h3>
    <p>We'll periodically announce "smoke sessions" via social media &amp; email where you can place an order for a particular weekend.  For example, we may announce a "Brisket Smoke Session" we'll offer Brisket with a choice of sides.  The day of the "session", our customers will be able to come pick up..</p>
  </article>
</section>

<section class="section menu">
  <h2 class="heading">Our Menu</h2>
  <p class="menu-intro">We're still in the process of building this out but I've listed what we currently offer &amp; what we'll offer in the very near future. Our specialty is smoked meats, however, we'll introduce sides when we come across something noteworthy</p>
  <div class="dish" style="left:77px">
    <div class="dish-photo" role="img" aria-label="Glazed beef short ribs on a plate" style="background:radial-gradient(circle at 50% 55%,#6a2e1a,#2a1410 75%)"></div>
    <h4>Beef Short Ribs</h4><div class="price">$20/lb</div>
    <p>Sed ut perspiciatis unde omnis iste natus error sit voluptatem accusantium doloremque laudantium</p>
  </div>
  <div class="dish" style="left:341px">
    <div class="dish-photo" role="img" aria-label="Beef back ribs with a side of beans" style="background:radial-gradient(circle at 50% 60%,#8a4224,#3a2014 75%)"></div>
    <h4>Beef Back Ribs</h4><div class="price">$18/lb</div>
    <p>Sed ut perspiciatis unde omnis iste natus error sit voluptatem accusantium doloremque laudantium</p>
  </div>
  <div class="dish" style="left:604px">
    <div class="dish-photo" role="img" aria-label="Sliced smoked beef brisket with vegetables" style="background:radial-gradient(circle at 50% 50%,#b04a45,#6a2a22 75%)"></div>
    <h4>Beef Brisket</h4><div class="price">$22/lb</div>
    <p>Sed ut perspiciatis unde omnis iste natus error sit voluptatem accusantium doloremque laudantium</p>
  </div>
  <div class="dish" style="left:866px">
    <div class="dish-photo" style="background:radial-gradient(circle at 50% 70%,#b8561a,#3a1a0c 75%)"><span class="soon">Coming<br>Soon</span></div>
    <h4>Chicken</h4><div class="price">$22/lb</div>
    <p>Sed ut perspiciatis unde omnis iste natus error sit voluptatem accusantium doloremque laudantium</p>
  </div>
</section>

<section class="section events">
  <h2 class="heading">Events</h2>
  <div class="event" style="left:99px">
    <div class="event-thumb" role="img" aria-label="Grilled meat close-up" style="background:linear-gradient(135deg,#7a4a2a,#2e1a10)"></div>
    <div class="event-name">Dale Mercer</div><div class="event-city">City name</div><div class="event-date">28 July, 2017</div>
    <p>Phasellus nisl est, condimentum vitae faucibus in, sollicitudin vel metus. Nunc sit amet consequat risus. Curabitur ac elit leo. In eleifend dui tellus, in scelerisque elit porttitor.</p>
  </div>
  <div class="event" style="left:451px">
    <div class="event-thumb" role="img" aria-label="Plated barbecue dish" style="background:linear-gradient(135deg,#a0522d,#4a2414)"></div>
    <div class="event-name">Dale Mercer</div><div class="event-city">City name</div><div class="event-date">28 July, 2017</div>
    <p>Phasellus nisl est, condimentum vitae faucibus in, sollicitudin vel metus. Nunc sit amet consequat risus. Curabitur ac elit leo. In eleifend dui tellus, in scelerisque elit porttitor.</p>
  </div>
  <div class="event" style="left:796px">
    <div class="event-thumb" role="img" aria-label="Sausages on a grill" style="background:linear-gradient(135deg,#8a4a30,#3a1e14)"></div>
    <div class="event-name">Dale Mercer</div><div class="event-city">City name</div><div class="event-date">28 July, 2017</div>
    <p>Phasellus nisl est, condimentum vitae faucibus in, sollicitudin vel metus. Nunc sit amet consequat risus. Curabitur ac elit leo. In eleifend dui tellus, in scelerisque elit porttitor.</p>
  </div>
  <div class="dots"><span></span><span></span><span></span><span></span></div>
</section>

<section class="section newsletter">
  <h2>JOIN OUR NEWSLETTER.</h2>
  <div class="email">email</div>
  <div class="btn join">JOIN NOW!</div>
</section>

<footer class="section footer">
  <div class="brand"><span class="mark"></span>Ember Ridge Smokehouse</div>
  <div class="col" style="left:374px;width:300px">
    <h5>Contact Us</h5>
    <div class="contact-row"><svg width="14" height="18" viewBox="0 0 14 18"><path d="M7 1a6 6 0 0 0-6 6c0 4.5 6 10 6 10s6-5.5 6-10a6 6 0 0 0-6-6z" fill="none" stroke="#ccc" stroke-width="1.5"/><circle cx="7" cy="7" r="2" fill="#ccc"/></svg><div>Ember Ridge Smokehouse<br>42 Cedar Hollow Road, Redwater</div></div>
    <div class="contact-row"><svg width="16" height="16" viewBox="0 0 24 24"><path fill="none" stroke="#ccc" stroke-width="1.8" d="M6.6 10.8a15.1 15.1 0 0 0 6.6 6.6l2.2-2.2 4.6 1.4V20A17 17 0 0 1 3 4h3.5l1.4 4.6z"/></svg><div>Phone<br>+1 (555) 014 2290</div></div>
    <div class="contact-row"><svg width="16" height="12" viewBox="0 0 16 12"><rect x="1" y="1" width="14" height="10" fill="none" stroke="#ccc" stroke-width="1.5"/><path d="M1 1l7 6 7-6" fill="none" stroke="#ccc" stroke-width="1.5"/></svg><div>hello@emberridgesmokehouse.example</div></div>
  </div>
  <div class="col" style="left:710px">
    <h5>Menu &amp; Pricing</h5>
    <div>Beef Short Ribs - $20/lb.</div><div>Beef Back Ribs - $18/lb.</div><div>Beef Brisket - $22/lb.</div>
    <div style="margin-top:22px">Coming soon</div><div>Chicken</div>
  </div>
  <div class="col" style="left:969px">
    <h5>Quick Links</h5>
    <div>Home</div><div>About me</div><div>Menu</div><div>Events</div><div>Preorder</div><div>Contact Us</div>
  </div>
  <div class="copyright">Copyright © Ember Ridge Smokehouse 2017. All rights reserved.</div>
  <div class="social"><span></span><span></span><span></span><span></span><span></span></div>
</footer>

</body>
</html>
```